Premium men's gut health supplement needs a bottle label designed

We’re velnora - a premium men’s wellness brand focused on gut health. Our first product is a high-quality daily supplement designed to support digestion, regularity, and internal cleanliness. Backed by science and tailored for modern lifestyles, velnora is crafted in the UK and proudly LGBT-owned. It aims to resolve intimacy problems that gay men may experience due to poor digestion but also does not exclude any other orientation - other men may use it simply to improve their digestion.

velnora is for health-conscious men who value science-backed supplements and want to feel confident from the inside out. Many of our early adopters will be gay and bisexual men who prioritise gut health as part of their self-care, sexual, and hygiene routine, though the product is equally effective and appealing to anyone seeking premium digestive support.

The product is premium the target customer is male, not specific to one location but primary markets will be US, UK and EU.

I’d like a supplement bottle designed for velnora, our premium men’s gut health brand. The focus should be clean, slightly clinical, and minimal - inspired by brands like Quelrin and Darvo. The key element is the wordmark (velnora) on the front, with no additional logo or icon. Lowercase text and a strong, contemporary font are preferred.

The bottle should be aesthetically pleasing so that people are proud to display it on their shelf, instead of hiding it in a cupboard (like Quelrin, darvo, Pia Venturek, Morvanel etc)

Avoid anything that shows the product as being for LGBT, e.g., no rainbows, men holding hands etc.

The design should be premium, minimalist and not be busy or overwhelming.

I have uploaded a file called "Bottle" to give an idea of the type of container, but please ignore the colours and change as you see fit. This is just for reference for the type of bottle we'll use - all colours are customisable.

I have also uploaded some images for "style" reference, e.g., darvo, quelrin, pia venturek, etc for inspiration.

```html
<!DOCTYPE html>
<html lang="en">
<head>
<meta charset="UTF-8">
<title>velnora — Gut Health Label</title>
<link href="https://fonts.googleapis.com/css2?family=Playfair+Display:wght@700;800&family=Montserrat:wght@400;500&family=Libre+Baskerville:wght@400&display=swap" rel="stylesheet">
<style>
  :root {
    --page-bg: #e4e4e4;
    --label-bg: #f3f3f3;
    --label-edge: #e2e2e2;
    --maroon: #6a1418;
    --maroon-deep: #560a0e;
    --maroon-soft: #8f4447;
    --ink: #2e2e33;
    --ink-soft: #4a4a50;
    --pill: #d9d9d9;
    --rule-grey: #b8b8b8;
  }
  * { margin: 0; padding: 0; box-sizing: border-box; }
  html, body {
    width: 1058px;
    height: 1200px;
    overflow: hidden;
    background: var(--page-bg);
  }
  .canvas {
    position: relative;
    width: 1058px;
    height: 1200px;
  }
  .label {
    position: absolute;
    left: 28px;
    top: 85px;
    width: 1002px;
    height: 1030px;
    background: linear-gradient(90deg, var(--label-edge) 0%, var(--label-bg) 18%, var(--label-bg) 82%, var(--label-edge) 100%);
  }
  .wordmark {
    position: absolute;
    left: 0;
    right: 0;
    top: 20px;
    text-align: center;
    font-family: "Playfair Display", serif;
    font-weight: 800;
    font-size: 172px;
    line-height: 1;
    letter-spacing: -5px;
    color: var(--maroon);
    white-space: nowrap;
  }
  .tagline {
    position: absolute;
    left: 0;
    right: 0;
    top: 200px;
    text-align: center;
    font-family: "Montserrat", sans-serif;
    font-weight: 400;
    font-size: 40px;
    color: var(--ink);
    white-space: nowrap;
  }
  .gut-icon {
    position: absolute;
    left: 415px;
    top: 398px;
    width: 165px;
    height: 172px;
    border-radius: 28px;
    background: radial-gradient(circle at 45% 45%, #a8686a 0%, var(--maroon) 70%);
    opacity: 0.85;
  }
  .eyebrow {
    position: absolute;
    left: 176px;
    top: 602px;
    width: 652px;
    height: 50px;
  }
  .eyebrow-line {
    position: absolute;
    top: 24px;
    height: 3px;
    width: 95px;
    background: var(--rule-grey);
  }
  .eyebrow-line.left { left: 0; }
  .eyebrow-line.right { right: 0; }
  .eyebrow-pill {
    position: absolute;
    left: 120px;
    top: 0;
    width: 410px;
    height: 50px;
    border-radius: 25px;
    background: var(--pill);
    font-family: "Montserrat", sans-serif;
    font-weight: 500;
    font-size: 39px;
    line-height: 50px;
    text-align: center;
    color: var(--ink);
    white-space: nowrap;
  }
  .product-name {
    position: absolute;
    left: 0;
    right: 0;
    top: 668px;
    text-align: center;
    font-family: "Playfair Display", serif;
    font-weight: 700;
    font-size: 134px;
    line-height: 1;
    letter-spacing: -2px;
    color: var(--maroon);
    white-space: nowrap;
  }
  .benefit-band {
    position: absolute;
    left: 172px;
    top: 811px;
    width: 656px;
    height: 128px;
    border-top: 3px solid var(--maroon-soft);
    border-bottom: 3px solid var(--maroon-soft);
  }
  .benefit-list {
    position: absolute;
    left: 0;
    top: 24px;
    font-family: "Montserrat", sans-serif;
    font-weight: 400;
    font-size: 29px;
    line-height: 39px;
    color: var(--ink-soft);
    white-space: nowrap;
  }
  .benefit-tag {
    position: absolute;
    right: 0;
    top: -10px;
    width: 196px;
    height: 135px;
    padding: 30px 0 0 26px;
    background: linear-gradient(90deg, var(--maroon-deep) 0%, var(--maroon-soft) 100%);
    font-family: "Montserrat", sans-serif;
    font-weight: 400;
    font-size: 29px;
    line-height: 39px;
    color: #f4e9e9;
    white-space: nowrap;
  }
  .product-meta {
    position: absolute;
    left: 174px;
    width: 654px;
    top: 962px;
    display: flex;
    justify-content: space-between;
    align-items: center;
    font-family: "Libre Baskerville", serif;
    font-weight: 400;
    font-size: 33px;
    line-height: 1.2;
    color: var(--ink);
    white-space: nowrap;
  }
</style>
</head>
<body>
  <div class="canvas">
    <section class="label">
      <h1 class="wordmark">velnora</h1>
      <p class="tagline">Male Entrepreneurial Health</p>

      <div class="gut-icon" role="img" aria-label="Icon of intestines with a protective shield and tick"></div>

      <div class="eyebrow">
        <span class="eyebrow-line left"></span>
        <span class="eyebrow-pill">Premium Men’s</span>
        <span class="eyebrow-line right"></span>
      </div>

      <h2 class="product-name">Gut Health</h2>

      <div class="benefit-band">
        <p class="benefit-list">Supports Men’s Wellness<br>Immune &amp; Digestive Health</p>
        <p class="benefit-tag">Probiotics<br>For Men</p>
      </div>

      <p class="product-meta">
        <span>Dietary Supplement</span>
        <span>|</span>
        <span>60 Capsules</span>
      </p>
    </section>
  </div>
</body>
</html>
```